New Years Greeting Card Design Competition

We need a greeting card design for the new year 2014. We would like to have pictures of our daughter Meera on the card. Please find attached 5 photos of her. Please feel free to use all 5 or some of them for the design. We would like the following text on the card: "Happy New Year" and "Vik, Pooja, and Meera Deshpande." We would like to see designs that are very positive in style.

Target Market(s)

The greeting card is going to be sent to family and friends in different parts of the world.

Requirements
Must have
• We would like to have pictures of our daughter Meera on the card. Please find attached 5 photos of her. Please feel free to use all 5 or some of them for the design. We would like the following text on the card: "Happy New Year" and "Vik, Pooja, and Meera Deshpande."

```html
<!DOCTYPE html>
<html lang="en">
<head>
<meta charset="utf-8">
<title>Happy New Year 2014 – Vik, Pooja, and Meera Deshpande</title>
<link rel="stylesheet" href="https://fonts.googleapis.com/css2?family=Marcellus&family=Crimson+Text&family=Libre+Baskerville:wght@700&display=swap">
<style>
  :root {
    --card-bg: #6d6570;
    --card-edge: #a7a2a8;
    --bokeh: rgba(255,255,255,0.10);
    --teal: #7fcdcf;
    --teal-frame: #5fb7bf;
    --coral: #e8775c;
    --coral-frame: #e98a72;
    --lavender-frame: #a496cc;
    --white: #ffffff;
    --cream: #f6e7b4;
    --blanket: #a99ad6;
  }
  html, body {
    margin: 0;
    padding: 0;
    width: 1200px;
    height: 778px;
    overflow: hidden;
    background: var(--card-edge);
  }
  .card {
    position: relative;
    width: 1190px;
    height: 768px;
    margin: 5px;
    overflow: hidden;
    background:
      radial-gradient(circle at 90px 40px, var(--bokeh) 0 60px, transparent 61px),
      radial-gradient(circle at 240px 700px, var(--bokeh) 0 70px, transparent 71px),
      radial-gradient(circle at 480px 720px, var(--bokeh) 0 55px, transparent 56px),
      radial-gradient(circle at 640px 120px, var(--bokeh) 0 50px, transparent 51px),
      radial-gradient(circle at 60px 520px, var(--bokeh) 0 75px, transparent 76px),
      radial-gradient(circle at 720px 640px, var(--bokeh) 0 65px, transparent 66px),
      radial-gradient(ellipse at 30% 50%, #7a727d, var(--card-bg) 70%);
  }
  .hero-photo {
    position: absolute;
    right: 0;
    top: 0;
    width: 520px;
    height: 768px;
    background: linear-gradient(180deg, #e9e6ee 0%, #d8cfd6 35%, var(--blanket) 55%, #b9addf 100%);
    -webkit-mask-image: linear-gradient(90deg, transparent 0, #000 110px);
    mask-image: linear-gradient(90deg, transparent 0, #000 110px);
  }
  .snapshot {
    position: absolute;
    margin: 0;
    box-sizing: border-box;
    box-shadow: 0 4px 10px rgba(0,0,0,0.35);
  }
  .snapshot .mat {
    position: absolute;
    background: var(--white);
  }
  .snapshot .photo {
    position: absolute;
    inset: 10px;
  }
  .snapshot--teal {
    left: 14px; top: 42px; width: 320px; height: 425px;
    background: var(--teal-frame);
    transform: rotate(-4deg);
  }
  .snapshot--teal .mat { inset: 22px 24px 24px 22px; }
  .snapshot--teal .photo { background: linear-gradient(160deg, #d9dde0, #c46a93 70%, #e2e2e2); }
  .snapshot--coral {
    left: 330px; top: 14px; width: 335px; height: 440px;
    background: var(--coral-frame);
    transform: rotate(4deg);
  }
  .snapshot--coral .mat { inset: 22px; }
  .snapshot--coral .photo { background: linear-gradient(180deg, #f7d6c6, #e9c2a5 45%, #f4e6e3 70%, #f3dedd); }
  .snapshot--lavender {
    left: 552px; top: 252px; width: 206px; height: 232px;
    background: var(--lavender-frame);
    transform: rotate(-3deg);
  }
  .snapshot--lavender .mat { inset: 12px; }
  .snapshot--lavender .photo { inset: 8px; background: linear-gradient(180deg, #2b2a2e, #b9b0ad 40%, #5a4a4e 70%, #cfd2dc); }

  .type-layer {
    position: absolute;
    inset: 0;
    width: 1190px;
    height: 768px;
  }
  .greeting { font-family: "Marcellus", serif; font-weight: 400; }
  .greeting__happy { fill: var(--teal); }
  .greeting__new { fill: var(--white); }
  .greeting__year { fill: var(--coral); }
  .year-number {
    font-family: "Libre Baskerville", serif;
    font-weight: 700;
    fill: var(--cream);
    filter: drop-shadow(0 2px 3px rgba(0,0,0,0.3));
  }
  .divider { fill: var(--teal); }
  .family {
    font-family: "Crimson Text", serif;
    font-size: 34px;
    fill: var(--white);
  }
</style>
</head>
<body>
  <main class="card">
    <div class="hero-photo" role="img" aria-label="Close-up photo of baby Meera wrapped in a lavender blanket"></div>

    <figure class="snapshot snapshot--teal">
      <div class="mat"><div class="photo" role="img" aria-label="Photo of Meera in a pink outfit lying in a patterned bouncer"></div></div>
    </figure>
    <figure class="snapshot snapshot--coral">
      <div class="mat"><div class="photo" role="img" aria-label="Photo of Meera in a bassinet under a floral blanket"></div></div>
    </figure>
    <figure class="snapshot snapshot--lavender">
      <div class="mat"><div class="photo" role="img" aria-label="Photo of Meera sleeping in a knit cap"></div></div>
    </figure>

    <svg class="type-layer" viewBox="0 0 1190 768" role="group" aria-label="Happy New Year 2014, Vik, Pooja, and Meera Deshpande">
      <g class="greeting">
        <text class="greeting__happy" x="57" y="548" font-size="112" textLength="66" lengthAdjust="spacingAndGlyphs">H</text>
        <text class="greeting__happy" x="120" y="505" font-size="92" textLength="208" lengthAdjust="spacingAndGlyphs">appy</text>
        <text class="greeting__new" x="334" y="550" font-size="126" textLength="92" lengthAdjust="spacingAndGlyphs">N</text>
        <text class="greeting__new" x="428" y="550" font-size="100" textLength="140" lengthAdjust="spacingAndGlyphs">ew</text>
        <text class="greeting__year" x="580" y="600" font-size="142" textLength="72" lengthAdjust="spacingAndGlyphs">Y</text>
        <text class="greeting__year" x="648" y="556" font-size="92" textLength="130" lengthAdjust="spacingAndGlyphs">ear</text>
      </g>

      <text class="year-number" x="788" y="625" font-size="262" textLength="378" lengthAdjust="spacingAndGlyphs">2014</text>

      <g class="divider" aria-hidden="true" transform="translate(150 576)">
        <circle cx="6" cy="12" r="3.5"/><circle cx="26" cy="12" r="3.5"/><circle cx="46" cy="12" r="4"/>
        <circle cx="66" cy="12" r="4"/><circle cx="86" cy="12" r="4.5"/><circle cx="106" cy="12" r="5"/>
        <circle cx="126" cy="12" r="5.5"/><circle cx="146" cy="12" r="6"/><circle cx="166" cy="12" r="6.5"/>
        <circle cx="186" cy="12" r="7"/><circle cx="208" cy="12" r="8"/><circle cx="235" cy="12" r="11"/>
        <circle cx="262" cy="12" r="8"/><circle cx="284" cy="12" r="7"/><circle cx="304" cy="12" r="6.5"/>
        <circle cx="324" cy="12" r="6"/><circle cx="344" cy="12" r="5.5"/><circle cx="364" cy="12" r="5"/>
        <circle cx="384" cy="12" r="4.5"/><circle cx="404" cy="12" r="4"/><circle cx="424" cy="12" r="4"/>
        <circle cx="444" cy="12" r="3.5"/><circle cx="464" cy="12" r="3.5"/><circle cx="484" cy="12" r="3"/>
        <circle cx="504" cy="12" r="3"/><circle cx="524" cy="12" r="3"/>
      </g>

      <text class="family" x="106" y="662">Vik, Pooja, and Meera Deshpande</text>
    </svg>
  </main>
</body>
</html>
```